Rosalind Vetteray Gymnastics Center Business Card

Develop a business card with my RV logo provided. A classy and unique design using the colors black, white, purple and maybe a splash of gold. Add Address (219 W. Lantern Ridge Road Medina, Ohio 44871), email (RosalindVetterayGymnasticsCtr@brellomail.com, website (www.RosalindVetterayGymnasticsCenter.example), phone number (216-555-0148) on the card. Social media if there's room also. t: @VetterayGym, i: @VetterayGym, f: @RosalindVetterayGymnasticsCenter

Target Market(s)

Families, children, gymnastics community and beyond

Industry/Entity Type

Business

Contact Information for Business Card

Add name (Rosalind Vetteray) who is the owner. Add logo, add address details, classy font, uniqueness important, rounded edges on business card. Horizontal business card needed.

Font styles to use
Serif
Sans Serif

Colors
6b449b
ffffff

Requirements
Must have
• Must have logo, owner name and owner on card, must have colors purple, white, black where needed in print, and a splash of gold if appropriate. Keep card classy and clean. Must have address of location, phone number, website of business, email and social media.
Nice to have
• I am open here, but I'd appreciate uniqueness. Must be a lasting image for branding...
Should not have
• No kid-like looks...

```html
<!DOCTYPE html>
<html lang="en">
<head>
<meta charset="utf-8">
<title>Rosalind Vetteray Gymnastics Center – Business Card</title>
<link href="https://fonts.googleapis.com/css2?family=Cinzel:wght@700&family=Lato:wght@400;700&family=Cormorant+Garamond:wght@500&display=swap" rel="stylesheet">
<style>
  :root {
    --purple: #6b449b;
    --purple-deep: #5f2d8a;
    --ink: #111111;
    --paper: #ffffff;
    --night: #08040a;
    --backdrop: #4a4a4c;
  }
  * { margin: 0; padding: 0; box-sizing: border-box; }
  html, body { width: 1189px; height: 1200px; overflow: hidden; }
  body { background: var(--backdrop); position: relative; font-family: "Lato", sans-serif; }

  .card { position: absolute; left: 171px; width: 857px; height: 490px; overflow: hidden; }
  .card--front { top: 65px; background: var(--paper); border-radius: 204px 24px 24px 24px; }
  .card--back {
    top: 626px; border-radius: 24px 196px 24px 24px;
    background: linear-gradient(180deg, var(--purple-deep) 0%, #3d1c5a 35%, #1c0c26 65%, var(--night) 100%);
  }

  .brand { position: absolute; display: flex; flex-direction: column; align-items: center; }
  .brand__mark { width: 118px; height: 118px; border-radius: 50%; background: var(--purple); margin-bottom: 12px; }
  .brand__name { font-family: "Cinzel", serif; font-weight: 700; font-size: 23px; line-height: 24px; text-align: center; letter-spacing: 0.5px; }
  .brand__rule { width: 100%; height: 1px; margin: 6px 0 3px; }
  .brand__tagline { font-family: "Cormorant Garamond", serif; font-weight: 500; font-size: 20px; letter-spacing: 0.6px; }

  .card--front .brand { right: 45px; top: 52px; width: 300px; }
  .card--front .brand__name { color: var(--ink); }
  .card--front .brand__rule { background: var(--purple); }
  .card--front .brand__tagline { color: var(--purple); }

  .card--back .brand { left: 50%; transform: translateX(-50%); top: 138px; width: 305px; }
  .card--back .brand__mark { background: var(--paper); }
  .card--back .brand__name, .card--back .brand__tagline { color: var(--paper); }
  .card--back .brand__rule { background: var(--paper); }

  .owner { position: absolute; left: 46px; top: 292px; }
  .owner__name { font-weight: 700; font-size: 26px; color: var(--ink); line-height: 28px; }
  .owner__role { font-size: 20px; color: var(--purple); line-height: 20px; }
  .divider { position: absolute; left: 46px; top: 357px; width: 764px; height: 1.5px; background: var(--purple); }

  .contacts { position: absolute; left: 46px; top: 370px; list-style: none; }
  .contacts li { display: flex; align-items: center; height: 29px; font-size: 20px; color: var(--ink); }
  .contacts svg { width: 20px; height: 20px; margin-right: 12px; fill: var(--purple); flex: none; }

  .social { position: absolute; left: 679px; top: 410px; display: flex; gap: 7px; }
  .social span { width: 39px; height: 39px; border-radius: 50%; display: block; }
  .social .t { background: #3d97d5; }
  .social .i { background: #1d4a6b; }
  .social .f { background: #4a69ad; }
</style>
</head>
<body>
  <section class="card card--front" aria-label="Card front">
    <div class="brand">
      <div class="brand__mark" aria-hidden="true"></div>
      <div class="brand__name">Rosalind Vetteray<br>Gymnastics Center</div>
      <div class="brand__rule"></div>
      <div class="brand__tagline">Gymnastics, Camps, Yoga &amp; More</div>
    </div>

    <div class="owner">
      <div class="owner__name">Rosalind Vetteray</div>
      <div class="owner__role">owner</div>
    </div>
    <div class="divider"></div>

    <ul class="contacts">
      <li><svg viewBox="0 0 24 24"><path d="M3 9c0-3 4-5 9-5s9 2 9 5v2h-5V9H8v2H3zM6 12h12l2 8H4zm6 2a2.5 2.5 0 1 0 0 5 2.5 2.5 0 0 0 0-5z"/></svg>(216-555-0148)</li>
      <li><svg viewBox="0 0 24 24"><path d="M2 5h20v14H2zm2 2v.5l8 6 8-6V7l-8 6z"/></svg>RosalindVetterayGymnasticsCtr@brellomail.com</li>
      <li><svg viewBox="0 0 24 24"><path d="M12 2a10 10 0 1 0 0 20 10 10 0 0 0 0-20zm0 2c1.2 1.5 2 3.6 2.2 6H9.8c.2-2.4 1-4.5 2.2-6zM4.1 10a8 8 0 0 1 4-5.2A12 12 0 0 0 7.8 10zm0 4h3.7a12 12 0 0 0 .3 5.2 8 8 0 0 1-4-5.2zM9.8 14h4.4c-.2 2.4-1 4.5-2.2 6-1.2-1.5-2-3.6-2.2-6zm6.4 0h3.7a8 8 0 0 1-4 5.2 12 12 0 0 0 .3-5.2zm0-4a12 12 0 0 0-.3-5.2 8 8 0 0 1 4 5.2z"/></svg>www.RosalindVetterayGymnasticsCenter.example</li>
    </ul>

    <div class="social" role="img" aria-label="Social media: @VetterayGym, @VetterayGym, @RosalindVetterayGymnasticsCenter">
      <span class="t"></span><span class="i"></span><span class="f"></span>
    </div>
  </section>

  <section class="card card--back" aria-label="Card back">
    <div class="brand">
      <div class="brand__mark" aria-hidden="true"></div>
      <div class="brand__name">Rosalind Vetteray<br>Gymnastics Center</div>
      <div class="brand__rule"></div>
      <div class="brand__tagline">Gymnastics, Camps, Yoga &amp; More</div>
    </div>
  </section>
</body>
</html>
```